Business Card Design

I need a business card for my rental business. The business is named:
Cruise a Trikeway Houston
www.cruiseatrikewayhouston.com
(832) 555-0193
This will be a business card that I will leave at other businesses as advertisement so it needs to have the name, website, and phone number.
Please feel free to be creative. This is a new business so I have no designs.
Thank you very much for your time and I look forward to receiving your designs
Target Market(s)
Local rental customers
Industry/Entity Type
Business
Contact Information for Business Card
Please check out my website:
Font styles to use
Other font styles liked:
- anything creative
Colors
Designer to choose colors to be used in the design.
Requirements
Must have
- Business name, phone, website. Rentals available hourly or daily. Book online

```html
<!DOCTYPE html>
<html lang="en">
<head>
<meta charset="utf-8">
<title>Cruise a Trikeway Houston — Business Card</title>
<link rel="stylesheet" href="https://fonts.googleapis.com/css2?family=Russo+One&family=Fira+Sans+Condensed:wght@400;600&display=swap">
<style>
  :root {
    --bg: #ece9e4;
    --brand-red: #c21f26;
    --paper: #ffffff;
    --ink: #111111;
  }
  html, body { margin: 0; padding: 0; overflow: hidden; }
  body {
    width: 1200px; height: 900px;
    background: var(--bg);
    display: flex; align-items: center; justify-content: center; gap: 40px;
  }
  .card {
    width: 540px; height: 309px;
    background: var(--paper);
    box-shadow: 0 6px 18px rgba(0,0,0,.18);
    display: block;
  }
  .title { font-family: "Russo One", sans-serif; font-size: 28px; letter-spacing: .4px; fill: var(--ink); }
  .small { font-family: "Fira Sans Condensed", sans-serif; fill: var(--paper); }
  .cta { font-family: "Russo One", sans-serif; font-size: 14px; fill: var(--paper); }
  .red { fill: var(--brand-red); }
  .white { fill: var(--paper); }
  .ink { fill: var(--ink); }
  .stripe { stroke: var(--paper); stroke-width: 5; }
  .bar { stroke: var(--ink); stroke-width: 3; }
  .icon-line { fill: none; stroke: var(--paper); stroke-width: 1.5; }
</style>
</head>
<body>

  <!-- Front -->
  <svg class="card card--front" viewBox="0 0 540 309" aria-label="Business card front">
    <rect class="white" width="540" height="309"/>
    <polygon class="red" points="0,80 300,40 540,40 540,309 0,309"/>
    <g class="stripes">
      <line class="stripe" x1="0" y1="62" x2="540" y2="108"/>
      <line class="stripe" x1="0" y1="76" x2="540" y2="122"/>
      <line class="stripe" x1="0" y1="90" x2="540" y2="136"/>
    </g>
    <polygon class="white" points="0,142 490,142 490,178 0,186"/>
    <text class="title" x="18" y="172">CRUISE A TRIKEWAY HOUSTON</text>
    <text class="small" x="150" y="208" font-size="13">www.cruiseatrikewayhouston.com</text>
  </svg>

  <!-- Back -->
  <svg class="card card--back" viewBox="0 0 540 309" aria-label="Business card back">
    <rect class="red" width="540" height="309"/>
    <polygon class="white" points="0,130 0,309 300,309"/>
    <g class="stripes">
      <line class="stripe" x1="0" y1="150" x2="359" y2="309"/>
      <line class="stripe" x1="18" y1="150" x2="377" y2="309"/>
      <line class="stripe" x1="36" y1="150" x2="395" y2="309"/>
    </g>

    <rect class="white" x="0" y="108" width="482" height="40"/>
    <text class="title" x="18" y="138">CRUISE A TRIKEWAY HOUSTON</text>

    <g class="book-online">
      <rect class="ink" x="262" y="158" width="212" height="26"/>
      <text class="cta" x="271" y="176">BOOK YOUR RIDE ONLINE</text>
      <line class="bar" x1="480" y1="158" x2="480" y2="184"/>
      <line class="bar" x1="486" y1="158" x2="486" y2="184"/>
      <line class="bar" x1="492" y1="158" x2="492" y2="184"/>
    </g>
    <text class="small" x="262" y="206" font-size="13">www.cruiseatrikewayhouston.com</text>
    <text class="small" x="262" y="221" font-size="10">Rentals available hourly and daily</text>

    <g class="contact-phone">
      <path class="white" d="M410 32c2 0 3 4 2 5l-2 1c1 3 3 5 6 6l1-2c1-1 5 0 5 2l-1 3c-8 0-14-6-14-14z"/>
      <text class="small" x="515" y="44" font-size="13" text-anchor="end">(832) 555-0193</text>
    </g>
    <g class="contact-email">
      <rect class="icon-line" x="350" y="272" width="16" height="12"/>
      <polyline class="icon-line" points="350,272 358,279 366,272"/>
      <text class="small" x="515" y="283" font-size="13" text-anchor="end">hello@cruiseatrikeway.com</text>
    </g>
  </svg>

</body>
</html>
```